Board menu for "Olla Dorada" food truck

Summary
**********************************
We need a menu design for a food truck. The menu will be printed and placed in the food truck side, so that customers can read it while standing one or two meters away from it. The size of the printed menu should be (width x height): 108cm x 70cm. The food truck is located in Panama and the menu language is Spanish.

Menu Sections
**************************************
The menu is divided in the following 5 sections:

1. Main Courses: This section should take most of the menu space. There are 5 menu items in this section. Each item has a Name, Description, Picture, Price (of item alone), and Price (of item in combo). Please note that for all items, combo means adding one beverage and one side. The added price is $1.50 to make any main course a combo. So it might we better to say “make it a combo for +$1.50” versus say “alone $5.50, in combo $7.00”.

2. Side Orders: This section has 2 menu items. Each item has a Name and Price. There are no pictures for this section or items.

3. Soups: This section has a Picture and Description for the entire section plus 2 menu items. Each menu item has a Name and Price.

4. Bakery: This section has a Picture for the entire section plus 5 menu items. Each item has a Name and a Price.

5. Beverages: This section has 5 menu items. Each menu item has a Name and a Price. There are no pictures for this section or items.

Attachments
*******************************************
We are attaching a zip file with picture of the exterior of the food truck. The menu will go in the space between the food truck’s window and the light switch, leaving ample space between those boundaries and the menu. The trash can shown in the picture has been relocated so it will not obstruct the menu view.

The zip file also contains the pictures for the 5 menu items in the Main Courses section, the picture for the Soups section, and the picture for the Bakery section (the bakery picture is provided as a place holder. We will provide a better bakery picture to the winning design to replace this one). For information purposes, the zip file also contains the food truck logo. The logo will not go in the menu. The brand and social media icons will go elsewhere in the truck.

The zip file also contains the file “menu information.xlsx”. This file has the following sheets:

Sections: Contains a column with the section name in English and another one with the section name in Spanish (which should be used in the menu). For the Soups section, contains a column with the section’s Description and Picture Name. For the Bakery section, contains a column with the section’s Picture Name.

Main Courses: Contains a column for each of the following: Item Name, Item Description, Item Picture Name, Item Price, Item Price (in combo). Again, we leave it to the designer’s discretion to use +$1.50 (or similar) for the combo versus publishing the full combo price.

Side Orders: Contains columns for Item Name and Item Price.

Soups: Contains columns for Item Name and Item Price.

Bakery: Contains columns for Item Name and Item Price. In the case of the Donuts item, there is an addition column with the Available Flavors.

Beverages: Contains columns for Item Name and Item Price. In the case of the Sodas item, there is an additional column with the Available Flavors.

A note about file encoding: the excel file contains texts with Spanish language special characters. It is encoded in the Windows-1252 encoding which I think is the Excel default for Western European languages. For those having trouble with this encoding, I included a “menu information csv” folder in the zip file with all the sheets in csv format encoded using UTF-8.
Updates

Target Market(s)

The truck sells fast food to drivers commuting from Panama City to towns in the west of the city. The average customer is a middle-class professional with a car. The truck is located in one of our gas stations so most customers stop to fuel their cars and grab something to eat for the ride home.

Font styles to use
Sans Serif

Colors

Designer to choose colors to be used in the design.

Requirements
Must have
• We would like to make emphasis in the main courses. Since they required preparation, they are not displayed, unlike other items like bakery, soups and beverages that are always ready and displayed. Having their pictures and descriptions on the menu will allows the customer to quickly figure out what main courses are available.

```html
<!DOCTYPE html>
<html lang="es">
<head>
<meta charset="utf-8">
<title>Olla Dorada — Menú</title>
<link href="https://fonts.googleapis.com/css2?family=Teko:wght@400;500;600&family=Open+Sans:wght@400;600&family=Courgette&display=swap" rel="stylesheet">
<style>
:root{
  --page:#d9d9d9;
  --board-a:#2f2f2f;
  --board-b:#5b5b5b;
  --green-dark:#2c6b2e;
  --green:#3f8a3c;
  --green-light:#5aa24f;
  --mint:#dbe9da;
  --ink:#2f3a30;
  --white:#ffffff;
}
*{margin:0;padding:0;box-sizing:border-box}
html,body{width:1200px;height:1057px;overflow:hidden;background:var(--page)}
.menu{position:absolute;left:20px;top:152px;width:1160px;height:752px;
  background:linear-gradient(135deg,var(--board-b),var(--board-a) 45%,var(--board-b));
  box-shadow:0 10px 24px rgba(0,0,0,.35);font-family:"Open Sans",sans-serif;color:var(--ink)}
.section-title{position:absolute;font-family:"Teko",sans-serif;font-weight:500;color:var(--white);
  font-size:26px;letter-spacing:1px;line-height:1}
.main-title{left:0;width:100%;top:6px;text-align:center;font-size:27px}
.card{position:absolute;top:34px;width:222px;height:405px}
.card-photo{position:absolute;left:0;top:0;width:222px;height:224px;background:linear-gradient(160deg,#b9795a,#e6c39a 50%,#c23a3a)}
.card-name{position:absolute;left:0;top:0;width:222px;height:30px;padding-left:8px;
  background:linear-gradient(90deg,var(--green-dark),var(--green-light));border-bottom-right-radius:40px 16px;
  font-family:"Courgette",cursive;font-weight:400;color:var(--white);font-size:17px;line-height:30px;white-space:nowrap}
.card-desc{position:absolute;left:0;top:224px;width:222px;height:118px;
  background:linear-gradient(170deg,var(--green-dark) 0%,var(--green) 35%,var(--green-light) 50%,var(--green) 65%,var(--green-dark) 100%);
  color:var(--white);text-align:center;display:flex;align-items:center;justify-content:center;
  font-size:15.5px;line-height:20px;padding:0 4px}
.card-desc.small{font-size:13.5px;line-height:18px}
.price-row{position:absolute;left:0;top:344px;width:222px;height:61px;display:flex;gap:6px}
.price{flex:1;background:var(--mint);text-align:center}
.price-label{display:block;margin:3px 6px 0;background:var(--green-dark);color:var(--white);
  font-size:9px;font-weight:600;line-height:14px}
.price-value{display:block;font-size:23px;line-height:40px;color:#3a3a3a}
.panel{position:absolute;top:474px;height:262px;width:336px;background:var(--green-dark)}
.panel-photo{height:172px}
.soup-photo{background:linear-gradient(120deg,#c8404a,#e8e0c8 40%,#1a1a1a 60%)}
.pastry-photo{background:radial-gradient(circle at 55% 45%,#d79a52,#a8652c 55%,#2a2a2a)}
.panel-list{position:absolute;left:4px;right:4px;top:172px;bottom:6px;background:var(--mint);
  font-family:"Teko",sans-serif;font-size:17px;line-height:1}
.item{position:absolute;white-space:nowrap}
.item::before{content:"~ ";color:var(--ink)}
.note{position:absolute;font-family:"Teko",sans-serif;font-size:12px;line-height:11px;white-space:nowrap}
.sides{position:absolute;left:702px;top:474px;width:450px;height:123px;background:var(--green);border-radius:14px 10px 10px 14px}
.sides-box{position:absolute;left:0;top:0;width:420px;height:123px;background:var(--mint);border-radius:12px}
.drinks{position:absolute;left:702px;top:621px;width:450px;height:120px;background:var(--green);border-radius:14px 10px 10px 14px}
.drinks-box{position:absolute;left:0;top:0;width:420px;height:120px;background:var(--mint);border-radius:12px;
  font-family:"Teko",sans-serif;font-size:17px;line-height:1}
.big-item{position:absolute;font-family:"Teko",sans-serif;font-size:34px;line-height:1;color:#3a3f3a;letter-spacing:.5px;white-space:nowrap}
</style>
</head>
<body>
<main class="menu">
  <h1 class="section-title main-title">PLATOS PRINCIPALES</h1>

  <article class="card" style="left:9px">
    <div class="card-photo" role="img" aria-label="Foto del emparedado de jamón y queso"></div>
    <h2 class="card-name">La Esquinera</h2>
    <p class="card-desc">Emparedado<br>de queso americano<br>y jamones variados<br>en pan flauta,<br>a la plancha.</p>
    <div class="price-row"><div class="price"><span class="price-label">SOLO</span><span class="price-value">$2,50</span></div><div class="price"><span class="price-label">EN COMBO</span><span class="price-value">$4,00</span></div></div>
  </article>

  <article class="card" style="left:239px">
    <div class="card-photo" role="img" aria-label="Foto del choripán con chimichurri y papas"></div>
    <h2 class="card-name">El Chorizote</h2>
    <p class="card-desc">Choripan de<br>chorizo criollo jumbo<br>con chimichurri<br>de la casa en<br>pan baguette.</p>
    <div class="price-row"><div class="price"><span class="price-label">SOLO</span><span class="price-value">$3,00</span></div><div class="price"><span class="price-label">EN COMBO</span><span class="price-value">$4,50</span></div></div>
  </article>

  <article class="card" style="left:469px">
    <div class="card-photo" role="img" aria-label="Foto de patacones con pollo y salsa"></div>
    <h2 class="card-name">Patacón Dorado</h2>
    <p class="card-desc">Pollo, cebolla<br>caramelizada y salsa<br>de ajo con cilantro<br>sobre cama de<br>patacones.</p>
    <div class="price-row"><div class="price"><span class="price-label">SOLO</span><span class="price-value">$3,25</span></div><div class="price"><span class="price-label">EN COMBO</span><span class="price-value">$4,75</span></div></div>
  </article>

  <article class="card" style="left:699px">
    <div class="card-photo" role="img" aria-label="Foto del emparedado de pollo a la plancha"></div>
    <h2 class="card-name">El Preferido</h2>
    <p class="card-desc small">Emparedado de pollo<br>a la plancha, queso<br>mozzarella, cebolla<br>caramelizada, tomate<br>y salsa ranch en<br>pan baguette.</p>
    <div class="price-row"><div class="price"><span class="price-label">SOLO</span><span class="price-value">$4,50</span></div><div class="price"><span class="price-label">EN COMBO</span><span class="price-value">$6,00</span></div></div>
  </article>

  <article class="card" style="left:929px">
    <div class="card-photo" role="img" aria-label="Foto de hamburguesa con papas fritas"></div>
    <h2 class="card-name">La Parrandera</h2>
    <p class="card-desc small">1/2 libra de hamburguesa<br>Angus, queso americano,<br>cebolla caramelizada, tomate,<br>bacon y salsa de la casa<br>en pan de miel con<br>semillas de amapola.</p>
    <div class="price-row"><div class="price"><span class="price-label">SOLO</span><span class="price-value">$5,50</span></div><div class="price"><span class="price-label">EN COMBO</span><span class="price-value">$7,00</span></div></div>
  </article>

  <h2 class="section-title" style="left:9px;top:448px">SOPAS</h2>
  <section class="panel" style="left:9px">
    <div class="panel-photo soup-photo" role="img" aria-label="Foto de sopa de pollo en vaso"></div>
    <div class="panel-list">
      <span class="item" style="left:18px;top:8px">SOPA DE POLLO<br>&nbsp;&nbsp;&nbsp;&nbsp;CON ARROZ</span>
      <span style="position:absolute;left:256px;top:8px">$ 2,95</span>
      <span class="item" style="left:18px;top:48px">SOPA DE LENTEJA Y CARNE<br>&nbsp;&nbsp;&nbsp;&nbsp;CON ARROZ</span>
      <span style="position:absolute;left:256px;top:48px">$ 2,95</span>
    </div>
  </section>

  <h2 class="section-title" style="left:353px;top:448px">PASTELERÍA</h2>
  <section class="panel" style="left:353px">
    <div class="panel-photo pastry-photo" role="img" aria-label="Foto de empanadas y pastelitos horneados"></div>
    <div class="panel-list" style="font-size:14px">
      <span class="item" style="left:4px;top:6px">ENCHILADA DE CARNE</span><span style="position:absolute;left:140px;top:6px">$1,50</span>
      <span class="item" style="left:4px;top:28px">PASTELITO DE POLLO</span><span style="position:absolute;left:140px;top:28px">$1,25</span>
      <span class="item" style="left:4px;top:50px">PAÑUELO DE QUESO</span><span style="position:absolute;left:140px;top:50px">$1,00</span>
      <span class="item" style="left:4px;top:72px">CAÑÓN DE GUAYABA</span><span style="position:absolute;left:140px;top:72px">$0,85</span>
      <span class="item" style="left:190px;top:6px">DONAS RELLENAS</span>
      <span class="note" style="left:204px;top:22px">• CREMA PASTELERA<br>• FRESA<br>• MANZANA<br>• MARACUYÁ</span>
      <span style="position:absolute;left:292px;top:32px">$0,85</span>
    </div>
  </section>

  <h2 class="section-title" style="left:702px;top:448px">ACOMPAÑAMIENTOS</h2>
  <section class="sides">
    <div class="sides-box">
      <span class="big-item" style="left:22px;top:22px">~ PAPAS FRITAS</span><span class="big-item" style="left:312px;top:22px">$1,00</span>
      <span class="big-item" style="left:22px;top:70px">~ PATACONES</span><span class="big-item" style="left:312px;top:70px">$1,00</span>
    </div>
  </section>

  <h2 class="section-title" style="left:708px;top:597px;font-size:23px">BEBIDAS</h2>
  <section class="drinks">
    <div class="drinks-box">
      <span class="item" style="left:18px;top:10px">CHICHEME CHORRERANO (16OZ)</span><span style="position:absolute;left:218px;top:10px">$1,60</span>
      <span class="item" style="left:18px;top:38px">CHICA DEL DÍA (16OZ)</span><span style="position:absolute;left:218px;top:38px">$1,00</span>
      <span class="item" style="left:18px;top:66px">AGUA (16OZ)</span><span style="position:absolute;left:218px;top:66px">$0,75</span>
      <span class="item" style="left:18px;top:94px">CAFÉ DE ALTURA (8OZ)</span><span style="position:absolute;left:218px;top:94px">$1,00</span>
      <span class="item" style="left:270px;top:10px">SODAS (12OZ)</span>
      <span class="note" style="left:284px;top:28px">• COLA NEGRA<br>• COLA CERO<br>• FIZZ FRESA<br>• FIZZ MANZANA</span>
      <span style="position:absolute;left:374px;top:38px">$1,00</span>
    </div>
  </section>
</main>
</body>
</html>
```